Bright Ember Publicity is a new boutique Press Office with a small roster of well-chosen clients across an array of disciplines; from Art and Technology to Restaurants and Fashion. Based in Greenpoint Brooklyn, Bright Ember Publicity achieves outstanding results through hard work, tenacity, efficiency and a sense of humor. We need a simple, versatile and classic design. We would like each side of the card to be white text on a black background.

Boutique

```html
<!DOCTYPE html>
<html lang="en">
<head>
<meta charset="utf-8">
<title>Bright Ember Publicity — Business Cards</title>
<link rel="stylesheet" href="https://fonts.googleapis.com/css2?family=Cinzel:wght@500;600&family=Lato:wght@400;700&display=swap">
<style>
  :root {
    --backdrop: #2b2b2c;
    --card: #1e2024;
    --ink: #ffffff;
    --ink-soft: #f2f2f2;
  }
  * { box-sizing: border-box; margin: 0; padding: 0; }
  html, body {
    width: 1189px;
    height: 1200px;
    overflow: hidden;
    background: var(--backdrop);
  }
  .canvas {
    position: relative;
    width: 1189px;
    height: 1200px;
  }
  .card {
    position: absolute;
    left: 173px;
    width: 854px;
    background: var(--card);
    color: var(--ink);
    text-align: center;
    box-shadow: 0 6px 18px rgba(0,0,0,0.45);
  }
  .card--front { top: 68px; height: 487px; }
  .card--back  { top: 605px; height: 508px; }

  .card__block {
    position: absolute;
    left: 0;
    right: 0;
  }
  .brand-dot {
    display: block;
    margin: 0 auto;
    width: 64px;
    height: 64px;
    border-radius: 50%;
    background: var(--ink);
  }
  .brand-name {
    font-family: "Cinzel", serif;
    font-weight: 600;
    color: var(--ink);
    line-height: 1;
  }
  .brand-name__main {
    display: block;
    font-size: 50px;
    letter-spacing: 0.09em;
  }
  .brand-name__sub {
    display: block;
    font-size: 21px;
    letter-spacing: 0.55em;
    margin-top: 18px;
    padding-left: 0.55em;
  }
  .card--back .brand-name__sub { margin-top: 16px; }

  .person__name {
    font-family: "Cinzel", serif;
    font-weight: 600;
    font-size: 27px;
    letter-spacing: 0.02em;
    line-height: 1;
  }
  .person__role {
    font-family: "Lato", sans-serif;
    font-size: 22px;
    color: var(--ink-soft);
    margin-top: 6px;
  }
  .contact {
    font-family: "Lato", sans-serif;
    font-size: 22px;
    line-height: 30px;
    color: var(--ink-soft);
  }
  .contact__label {
    font-family: "Cinzel", serif;
    font-weight: 600;
    margin-right: 6px;
  }
</style>
</head>
<body>
<main class="canvas">

  <section class="card card--front" aria-label="Card front">
    <div class="card__block" style="top:110px;">
      <span class="brand-dot"></span>
    </div>
    <div class="card__block" style="top:280px;">
      <h1 class="brand-name">
        <span class="brand-name__main">Bright Ember</span>
        <span class="brand-name__sub">Publicity</span>
      </h1>
    </div>
  </section>

  <section class="card card--back" aria-label="Card back">
    <div class="card__block" style="top:78px;">
      <span class="brand-dot"></span>
    </div>
    <div class="card__block" style="top:197px;">
      <h2 class="brand-name">
        <span class="brand-name__main">Bright Ember</span>
        <span class="brand-name__sub">Publicity</span>
      </h2>
    </div>
    <div class="card__block person" style="top:316px;">
      <p class="person__name">MARA ELLISON</p>
      <p class="person__role">Chief Executive Officer</p>
    </div>
    <div class="card__block contact" style="top:404px;">
      <p><span class="contact__label">P:</span>555 014 2387</p>
      <p><span class="contact__label">E:</span>mara@brightember.com</p>
    </div>
  </section>

</main>
</body>
</html>
```